VMR business card

Need a business card for a company that provides instructional design and elearning development services. The website is here: http://vantmoro.studio/

I'm attaching a current logo, as well as the old business card design. While I like to keep it clean, the old design is too simplistic for my liking. The only idea I want to reuse from the old design is placing industry jargon on the back of the card, just need a better way to present it. But if you have other ideas for the back--feel free to experiment.

Please use the colors complementary to the color we have on the website. Thank you!

```html
<!DOCTYPE html>
<html lang="en">
<head>
<meta charset="utf-8">
<title>VMR business card</title>
<link rel="stylesheet" href="https://fonts.googleapis.com/css2?family=Nunito:wght@700;800&family=Roboto:wght@400;700;900&display=swap">
<style>
  :root {
    --backdrop: #e4e4e6;
    --card-white: #ffffff;
    --gold: #dccf90;
    --gold-deep: #c9b86a;
    --teal: #2bb5ad;
    --ink-white: #ffffff;
    --shadow: rgba(0, 0, 0, 0.18);
  }
  * { box-sizing: border-box; margin: 0; padding: 0; }
  html, body { width: 1200px; height: 800px; overflow: hidden; }
  body {
    background: var(--backdrop);
    position: relative;
    font-family: "Roboto", Arial, sans-serif;
  }
  .card {
    position: absolute;
    width: 540px;
    height: 310px;
    border-radius: 22px;
    overflow: hidden;
    box-shadow: 0 6px 18px var(--shadow);
  }

  /* Front */
  .card-front { left: 610px; top: 110px; background: var(--card-white); }
  .front-panel { position: absolute; inset: 0; }
  .front-panel path { fill: var(--gold); }
  .brand {
    position: absolute;
    left: 20px; top: 40px;
    width: 120px; height: 230px;
    display: flex; flex-direction: column; align-items: center; justify-content: flex-end;
    gap: 14px;
  }
  .brand-name {
    writing-mode: vertical-rl;
    transform: rotate(180deg);
    font-family: "Nunito", Arial, sans-serif;
    font-weight: 800;
    font-size: 52px;
    letter-spacing: 4px;
    color: var(--gold-deep);
  }
  .brand-mark { width: 22px; height: 22px; background: var(--teal); }
  .holder-name {
    position: absolute;
    left: 195px; top: 48px;
    font-family: "Nunito", Arial, sans-serif;
    font-weight: 800;
    font-size: 38px;
    color: var(--ink-white);
    letter-spacing: 0.5px;
  }
  .contact-list {
    position: absolute;
    left: 185px; top: 135px;
    list-style: none;
    display: flex; flex-direction: column; gap: 14px;
  }
  .contact-item {
    display: flex; align-items: center; gap: 12px;
    font-size: 21px;
    color: var(--ink-white);
  }
  .contact-icon { width: 24px; height: 22px; flex: none; }
  .contact-icon * { fill: none; stroke: var(--ink-white); stroke-width: 2; }
  .contact-icon .solid { fill: var(--ink-white); stroke: none; }

  /* Back */
  .card-back {
    left: 60px; top: 380px;
    background: var(--teal);
    color: var(--ink-white);
    padding: 34px 30px;
    display: flex; flex-direction: column; justify-content: center;
    font-weight: 700;
  }
  .jargon {
    font-size: 23px;
    line-height: 1.2;
    letter-spacing: 0.3px;
    text-transform: uppercase;
  }
  .headline {
    font-weight: 900;
    font-size: 50px;
    line-height: 1.15;
    margin: 10px 0;
    letter-spacing: 0.5px;
  }
</style>
</head>
<body>
  <section class="card card-front" aria-label="Business card front">
    <svg class="front-panel" viewBox="0 0 540 310" width="540" height="310" aria-hidden="true">
      <path d="M160,0 H540 V310 H160 V205 L132,190 L160,180 V100 L132,85 L160,75 Z"/>
    </svg>
    <div class="brand">
      <span class="brand-name">VMR</span>
      <span class="brand-mark"></span>
    </div>
    <h1 class="holder-name">Daniel Korvath</h1>
    <ul class="contact-list">
      <li class="contact-item">
        <svg class="contact-icon" viewBox="0 0 24 22" aria-hidden="true">
          <path class="solid" d="M6 2 L10 6 L7.5 9 C9 12 11 14 14 15.5 L17 13 L21 17 L18 20 C10 19 4 12 3 5 Z"/>
        </svg>
        <span>555-013-4827</span>
      </li>
      <li class="contact-item">
        <svg class="contact-icon" viewBox="0 0 24 22" aria-hidden="true">
          <rect x="2" y="4" width="20" height="14"/>
          <path d="M2 4 L12 12 L22 4"/>
        </svg>
        <span>dkorvath@vantmoro.studio</span>
      </li>
      <li class="contact-item">
        <svg class="contact-icon" viewBox="0 0 24 22" aria-hidden="true">
          <rect x="2" y="2" width="20" height="13"/>
          <path d="M8 20 H16 M12 15 V20"/>
        </svg>
        <span>www.vantmoro.studio</span>
      </li>
    </ul>
  </section>

  <section class="card card-back" aria-label="Business card back">
    <p class="jargon">Mobile learning SCORM instructional<br>design LMS MOOCs eLearning HTML5</p>
    <h2 class="headline">HOW CAN WE HELP?</h2>
    <p class="jargon">Adult learning theory gamification<br>classroom xAPI blended learning</p>
  </section>
</body>
</html>
```